Coral Bay Dental Surgery Business Cards

Hi there

Can i please have a simple business card designed (front and back with a black background) using out white reverse logo and the same font used for the logo?
On the back we can just have the logo. Full details at the front part.
Here are the details:

Name of the surgery: Coral Bay | Dental Surgery
Name on the business card: Dr Owen Thackery
Credentials:
BDSc (KTL)
MSc Oral Implantology (Halvorsen, Frankfurt)
Fellow & Diplomate (Meridian Council of Restorative Prosthetics)

Email: owen.thackery@coralbaysmile.example
Address: 17 Lisgrove Rd Karrinyup
Website: coralbaysmile.example
Phone: 1800 316 482

We have attached our high res logo and a rudimentary version of the business card which is not necessarily what we want but gives all the details
We would like to have the print ready version. Thanks.

Contact Information for Business Card

website. credentials. qr code. address. phone number

Requirements
Must have
• QR code

```html
<!DOCTYPE html>
<html lang="en">
<head>
<meta charset="utf-8">
<title>Coral Bay Dental Surgery – Business Cards</title>
<link href="https://fonts.googleapis.com/css2?family=Poppins:wght@400;500;700;800&display=swap" rel="stylesheet">
<style>
  :root {
    --backdrop: #2b2d31;
    --card-black: #111214;
    --brand-teal: #2299b3;
    --accent-teal: #33bcc4;
    --rule-light: #d9dadc;
    --ink-light: #c9cbcf;
    --on-dark: #ffffff;
    --qr-frame: #ffffff;
  }
  * { margin: 0; padding: 0; box-sizing: border-box; }
  html, body {
    width: 1200px; height: 952px; overflow: hidden;
    background: var(--backdrop);
    font-family: "Poppins", sans-serif;
  }
  .canvas { position: relative; width: 1200px; height: 952px; }
  .card {
    position: absolute; left: 220px; width: 760px; height: 434px;
    overflow: hidden; background: var(--card-black);
  }
  .card-front { top: 26px; }
  .card-back { top: 494px; }
  .card-front .edge-lines { position: absolute; inset: 0; }
  .brand {
    position: absolute; display: flex; align-items: center; gap: 14px;
    font-weight: 500; line-height: 1.15; letter-spacing: 0.02em;
  }
  .brand-dot { width: 20px; height: 20px; border-radius: 50%; flex: none; }
  .card-front .brand { left: 70px; top: 128px; color: var(--brand-teal); font-size: 25px; }
  .card-front .brand-dot { background: var(--brand-teal); }
  .holder { position: absolute; left: 380px; top: 100px; }
  .holder-name {
    color: var(--accent-teal); font-weight: 800; font-size: 31px;
    letter-spacing: 0.01em; line-height: 1.1; white-space: nowrap;
  }
  .holder-role { color: var(--ink-light); font-size: 13px; font-weight: 500; margin-top: 4px; }
  .holder-rule { width: 70px; height: 2px; background: var(--ink-light); margin: 8px 0 16px; }
  .contact-list { list-style: none; }
  .contact-list li {
    display: flex; align-items: center; gap: 12px;
    color: var(--ink-light); font-size: 14px; margin-bottom: 9px; white-space: nowrap;
  }
  .contact-icon {
    width: 22px; height: 22px; border-radius: 4px; background: var(--brand-teal);
    display: flex; align-items: center; justify-content: center; flex: none;
  }
  .card-back .brand { left: 250px; top: 92px; color: var(--on-dark); font-size: 34px; }
  .card-back .brand-dot { background: var(--on-dark); width: 26px; height: 26px; }
  .qr-code {
    position: absolute; right: 40px; top: 40px; width: 96px; height: 96px;
    background: var(--qr-frame); border-radius: 6px;
  }
  .credentials { position: absolute; left: 110px; top: 232px; list-style: none; }
  .credentials li {
    display: flex; align-items: center; gap: 10px;
    color: var(--on-dark); font-size: 15px; margin-bottom: 12px;
  }
</style>
</head>
<body>
<main class="canvas">

  <section class="card card-front" aria-label="Business card front">
    <svg class="edge-lines" width="760" height="434" viewBox="0 0 760 434" aria-hidden="true">
      <line x1="0" y1="388" x2="332" y2="388" stroke="var(--accent-teal)" stroke-width="4"/>
      <line x1="332" y1="390" x2="760" y2="390" stroke="var(--rule-light)" stroke-width="8"/>
    </svg>

    <div class="brand">
      <span class="brand-dot"></span>
      <span>Coral Bay<br>Dental Surgery</span>
    </div>

    <div class="holder">
      <h1 class="holder-name">Dr OWEN THACKERY</h1>
      <p class="holder-role">Coral Bay | Dental Surgery</p>
      <div class="holder-rule"></div>
      <ul class="contact-list">
        <li>
          <span class="contact-icon">
            <svg width="12" height="14" viewBox="0 0 12 14"><path d="M6 0a5 5 0 0 0-5 5c0 3.8 5 9 5 9s5-5.2 5-9a5 5 0 0 0-5-5zm0 7a2 2 0 1 1 0-4 2 2 0 0 1 0 4z" fill="#fff"/></svg>
          </span>
          17 Lisgrove Rd Karrinyup
        </li>
        <li>
          <span class="contact-icon">
            <svg width="13" height="13" viewBox="0 0 24 24"><path d="M6.6 10.8a15.1 15.1 0 0 0 6.6 6.6l2.2-2.2c.3-.3.7-.4 1-.2 1.1.4 2.3.6 3.6.6.6 0 1 .4 1 1V20c0 .6-.4 1-1 1A17 17 0 0 1 3 4c0-.6.4-1 1-1h3.5c.6 0 1 .4 1 1 0 1.3.2 2.5.6 3.6.1.3 0 .7-.2 1z" fill="#fff"/></svg>
          </span>
          1800 316 482
        </li>
        <li>
          <span class="contact-icon">
            <svg width="14" height="10" viewBox="0 0 14 10"><rect x="0.7" y="0.7" width="12.6" height="8.6" fill="none" stroke="#fff" stroke-width="1.4"/><path d="M1 1l6 5 6-5" fill="none" stroke="#fff" stroke-width="1.4"/></svg>
          </span>
          owen.thackery@coralbaysmile.example
        </li>
        <li>
          <span class="contact-icon">
            <svg width="12" height="12" viewBox="0 0 12 12"><path d="M1 1l10 4-4 1.5L5.5 11z" fill="#fff"/></svg>
          </span>
          www.coralbaysmile.example
        </li>
      </ul>
    </div>
  </section>

  <section class="card card-back" aria-label="Business card back">
    <div class="brand">
      <span class="brand-dot"></span>
      <span>Coral Bay<br>Dental Surgery</span>
    </div>
    <div class="qr-code" role="img" aria-label="QR code linking to www.coralbaysmile.example"></div>
    <ul class="credentials">
      <li>
        <svg width="16" height="16" viewBox="0 0 16 16" aria-hidden="true"><rect x="1" y="3" width="11" height="11" fill="none" stroke="#fff" stroke-width="1.3"/><path d="M3.5 8l3 3 7-9" fill="none" stroke="#fff" stroke-width="1.6"/></svg>
        BDSc (KTL)
      </li>
      <li>
        <svg width="16" height="16" viewBox="0 0 16 16" aria-hidden="true"><rect x="1" y="3" width="11" height="11" fill="none" stroke="#fff" stroke-width="1.3"/><path d="M3.5 8l3 3 7-9" fill="none" stroke="#fff" stroke-width="1.6"/></svg>
        MSc Oral Implantology (Halvorsen, Frankfurt)
      </li>
      <li>
        <svg width="16" height="16" viewBox="0 0 16 16" aria-hidden="true"><rect x="1" y="3" width="11" height="11" fill="none" stroke="#fff" stroke-width="1.3"/><path d="M3.5 8l3 3 7-9" fill="none" stroke="#fff" stroke-width="1.6"/></svg>
        Fellow &amp; Diplomate (Meridian Council of Restorative Prosthetics)
      </li>
    </ul>
  </section>

</main>
</body>
</html>
```